BVH Business Card Design

We are a small construction equipment rental and hardware store located in Middle Tennessee. We have three stores. Our primary business is construction equipment. We have an existing logo we'd like to use. I think I would like to list each store physical address on the back of the card and maybe the web address also: www.bvhhireyard.example.

We also need a design that we can incorporate into company letterhead, small note pads, and even checks if possible.

Industry/Entity Type

Construction

Contact Information for Business Card

We have our Logo, Name: Brookvale Hauling Machinery, Employee Name, Main Phone Number, Mobile Phone Number, Email Address, Company Address, and website information (There are three locations that can go on the back if necessary) We would like to leave some room on the back of the card in case we want to write information down on it.

```html
<!DOCTYPE html>
<html lang="en">
<head>
<meta charset="utf-8">
<title>BVH Business Card – Back</title>
<link rel="stylesheet" href="https://fonts.googleapis.com/css2?family=Ubuntu:wght@300;400&display=swap">
<style>
  :root {
    --ink: #45607a;
    --band: #00148f;
    --band-text: #ffffff;
    --divider: #e2364a;
    --rule: #4a6078;
    --paper-light: #ffffff;
    --paper-edge: #e2e2e4;
  }
  html, body {
    margin: 0;
    padding: 0;
    overflow: hidden;
    background: #ffffff;
  }
  .card-back {
    position: relative;
    width: 1200px;
    height: 703px;
    overflow: hidden;
    background: radial-gradient(ellipse 75% 80% at 50% 45%, var(--paper-light) 0%, #f3f3f4 50%, var(--paper-edge) 100%);
    font-family: "Ubuntu", "Segoe UI", sans-serif;
    font-weight: 300;
    color: var(--ink);
  }
  .store {
    position: absolute;
    top: 74px;
    margin: 0;
    font-style: normal;
    font-size: 30px;
    line-height: 42px;
    white-space: nowrap;
  }
  .store .phone { display: block; margin-top: 7px; }
  .store--one { left: 62px; }
  .store--two { left: 398px; }
  .store--three { left: 814px; }
  .divider {
    position: absolute;
    top: 62px;
    width: 8px;
    height: 155px;
  }
  .divider--one { left: 361px; }
  .divider--two { left: 772px; }
  .web-band {
    position: absolute;
    top: 242px;
    left: 0;
    width: 1200px;
    height: 54px;
    background: var(--band);
    color: var(--band-text);
    font-size: 30px;
    line-height: 54px;
    text-align: center;
  }
  .note-lines {
    position: absolute;
    left: 60px;
    top: 0;
    width: 1080px;
    height: 703px;
  }
</style>
</head>
<body>
<main class="card-back">
  <address class="store store--one">418 Quarry Lane<br>Brookvale, TN 37011<span class="phone">(615) 555-0142</span></address>
  <svg class="divider divider--one" viewBox="0 0 8 155" aria-hidden="true">
    <defs>
      <pattern id="hatch" width="8" height="4" patternUnits="userSpaceOnUse">
        <line x1="0" y1="4" x2="8" y2="0" stroke="var(--divider)" stroke-width="1.3"/>
      </pattern>
    </defs>
    <rect width="8" height="155" fill="url(#hatch)"/>
  </svg>
  <address class="store store--two">27 Millstone Court<br>Ashbury Springs, TN 37088<span class="phone">(615) 555-0187</span></address>
  <svg class="divider divider--two" viewBox="0 0 8 155" aria-hidden="true">
    <rect width="8" height="155" fill="url(#hatch)"/>
  </svg>
  <address class="store store--three">2310 Route 52 North<br>Cedar Hollow, TN 37064<span class="phone">(615) 555-0163</span></address>

  <div class="web-band">www.bvhhireyard.example</div>

  <svg class="note-lines" viewBox="0 0 1080 703" aria-hidden="true">
    <g stroke="var(--rule)" stroke-width="1.5" stroke-dasharray="1.5 2.5">
      <line x1="0" y1="391" x2="1080" y2="391"/>
      <line x1="0" y1="474" x2="1080" y2="474"/>
      <line x1="0" y1="557" x2="1080" y2="557"/>
      <line x1="0" y1="640" x2="1080" y2="640"/>
    </g>
  </svg>
</main>
</body>
</html>
```